business card for training & coaching company, Brightwell.co

Create a warm, clean, professional 2-sided business card for Brightwell.co.
Brightwell.co is a new company that shares Brightwell Dialogue (combination of mindfulness, kindness, and nonviolent communication), training and coaching individuals and groups.
Include the logo provided, perhaps incorporating a second opaque version of it as well.
Feelings & Needs lists on the reverse side of the card.

Target Market(s)

Women 30-60 years old, university educated.
Spiritual, may be Buddhist.

Industry/Entity Type

Training

Contact Information for Business Card

Marisabel T. Oberholt, MSc
Group Facilitator & Certified Wellness Coach
Brightwell Dialogue training & support
Group Facilitator & Coach
01632 960 418
07700 900 862
www.brightwell-example.co

Font styles to use
Sans Serif

Requirements
Must have
• Front -- Contact details, logo provided.
• Back -- Feelings list; Needs list
• Professional yet warm, inviting, friendly feel.
Nice to have
• little graphics (telephone for phone number, envelope for email, globe for web);
• Clean font (like Sathu, Frutiga, Helvetica).
• Feeling of movement or transformation.
Should not have
• More than 3 colours.
• Loud or busy designs.
• A gentle curve or two is ok, but not swirly designs.
• No black or other heavy backgrounds.

```html
<!DOCTYPE html>
<html lang="en">
<head>
<meta charset="utf-8">
<title>Brightwell.co business card</title>
<link rel="stylesheet" href="https://fonts.googleapis.com/css2?family=Open+Sans:wght@400;600&display=swap">
<style>
  :root {
    --orange-light: #f3901f;
    --orange: #ee6d24;
    --orange-deep: #e8502c;
    --ink: #4a4a4a;
    --paper: #ffffff;
    --stage: #ecebe8;
  }
  * { box-sizing: border-box; margin: 0; padding: 0; }
  html, body {
    width: 1200px; height: 900px; overflow: hidden;
    background: var(--stage);
    font-family: "Open Sans", Arial, sans-serif;
  }
  .sheet {
    width: 1200px; height: 900px;
    display: flex; flex-direction: column; align-items: center; justify-content: center;
    gap: 30px;
  }
  .card {
    width: 720px; height: 411px; position: relative; overflow: hidden;
    box-shadow: 0 6px 18px rgba(0,0,0,0.12);
  }

  /* Reverse side */
  .card--back {
    background: linear-gradient(160deg, var(--orange-light) 0%, var(--orange) 50%, var(--orange-deep) 100%);
    color: var(--paper);
    display: flex; justify-content: space-around; align-items: center;
    padding: 0 50px;
  }
  .word-list { text-align: center; }
  .word-list__title {
    font-weight: 600; font-size: 30px; letter-spacing: 0.5px; margin-bottom: 22px;
  }
  .word-list__columns { display: flex; align-items: flex-start; gap: 22px; }
  .word-list__column { list-style: none; font-size: 21px; line-height: 29px; }
  .word-list__divider {
    width: 1.5px; height: 118px; background: rgba(255,255,255,0.85); margin-top: 6px;
  }

  /* Front side */
  .card--front {
    background: var(--paper);
    display: flex; flex-direction: column; align-items: center;
  }
  .brand {
    margin-top: 46px; display: flex; align-items: center; gap: 12px;
    color: var(--orange); font-weight: 600; font-size: 30px;
  }
  .brand__dot { width: 18px; height: 18px; border-radius: 50%; background: var(--orange); }
  .person__name {
    margin-top: 26px; color: var(--orange-deep); font-weight: 600; font-size: 30px;
  }
  .rule { width: 120px; height: 1.5px; background: var(--orange); margin: 8px 0 10px; }
  .person__role {
    color: var(--ink); font-size: 19px; line-height: 25px; text-align: center;
  }
  .contact {
    display: flex; gap: 26px; color: var(--ink); font-size: 20px;
  }
  .contact__sep { color: var(--ink); }
  .web-band {
    position: absolute; left: 0; right: 0; bottom: 0; height: 50px;
    background: linear-gradient(90deg, var(--orange-light), var(--orange-deep));
    color: var(--paper); font-weight: 600; font-size: 20px; letter-spacing: 4px;
    display: flex; align-items: center; justify-content: center;
  }
</style>
</head>
<body>
<main class="sheet">
  <section class="card card--back" aria-label="Card reverse: feelings and needs">
    <div class="word-list">
      <h2 class="word-list__title">Feeling</h2>
      <div class="word-list__columns">
        <ul class="word-list__column">
          <li>confusion</li><li>curious</li><li>despair</li><li>edgy</li><li>fiery</li><li>grief</li>
        </ul>
        <span class="word-list__divider"></span>
        <ul class="word-list__column">
          <li>nervous</li><li>powerless</li><li>shock</li><li>torn</li><li>weary</li><li>&amp; more…</li>
        </ul>
      </div>
    </div>
    <div class="word-list">
      <h2 class="word-list__title">Need</h2>
      <div class="word-list__columns">
        <ul class="word-list__column">
          <li>belonging</li><li>choice</li><li>clarity</li><li>empathy</li><li>freedom</li><li>meaning</li>
        </ul>
        <span class="word-list__divider"></span>
        <ul class="word-list__column">
          <li>mourning</li><li>peace</li><li>safety</li><li>support</li><li>understanding</li><li>&amp; more…</li>
        </ul>
      </div>
    </div>
  </section>

  <section class="card card--front" aria-label="Card front: contact details">
    <div class="brand"><span class="brand__dot"></span>Brightwell.co</div>
    <h1 class="person__name">Marisabel T. Oberholt</h1>
    <div class="rule"></div>
    <p class="person__role">MSc Group Facilitator &amp;<br>Certified Wellness Coach Brightwell Dialogue training &amp;<br>support Group Facilitator &amp; Coach</p>
    <div class="rule"></div>
    <p class="contact"><span>01632 960 418</span><span class="contact__sep">|</span><span>07700 900 862</span></p>
    <div class="web-band">www.brightwell-example.co</div>
  </section>
</main>
</body>
</html>
```